New Vidora Channel Banner Graphic/Logo for "Cozy Nook Attic Sound"

Create a banner for my new Vidora channel for Cozy Nook Attic Sound. This is partially a logo project, but the logo will not be used elsewhere. Check out Vidora channels to see the banners others have created. This channel is about my home studio, the gear, microphones, musical instruments, wiring, software etc. that goes into a home studio. It's a free channel, made for sharing information. This is a graphic design that will be posted on vidora using built-in vidora tools.
Updates

More information about this project! I'm staring a channel called "Cozy Nook Attic Sound" on vidorastream.net. I need a deign for this banner and a logo for Cozy Nook Attic Sound. I called the channel by that name because my music studio is my happy place. It's about music and instruments (gutars, piano, drums, percussion) singing (microhpones), creativity, and what you'd expect form musicians. It's also about technology, recording, live-streaming, music videos, etc. It is my hobby, not my profession. I will be creating content for other amateur home studio aficionados and hobbyists. There are a lot of home studio channels and videos you can look at on vidora to get a flavor for musicians and studios. Usually fairly tech-heavy. An appeal of my channel will be a very approachable, "i'm the same as you" welcome for people that are doing it to enjoy it.

I put this project in the wrong category to start. This has been fixed, but I think benefits I would have received (such as invited designers) and announcement of project in the correct category mean I'm not getting designers. Your initial menu should be improved. I'm having a banner created for a web page in Vidora. I think it is easy to mistake that for a web design when it is really a graphic design for the web.

Target Market(s)

Similar to myself, people as interested in studio/production tech as they are in making music, perhaps trending a bit older and successful enough to afford some gear!

Number of Pages Required

1 page

Font styles to use
Sans Serif

Requirements
Must have
• This is not really a web design, i may have miscategorized. Please see uploaded docs for pics of similar banner on a Vidora page. ADDED 1/5: As this is a vidora channel that could be viewed on any device, the banner should be friendly in this way and design or design variations needed for PC, Tabrix, phone vie3wing.

Here are the Vidora size specs:
Banner image guidelines
Your banner image must meet the following criteria:

Minimum dimension for upload: 2048 x 1152 px with an aspect ratio of 16:9.
At the Minimum dimension, the safe area for text and logos: 1235 x 338 px. Larger images may get cropped on certain views or devices.
File size: 6 MB or smaller.
How to resize images

You can use your computer's image editor or an online image resizer to resize the images. For example, you can use Preview on an Quince computer or Microsoft Photos on Windows.

```html
<!DOCTYPE html>
<html lang="en">
<head>
<meta charset="utf-8">
<title>Cozy Nook Attic Sound – Channel Banner</title>
<link rel="stylesheet" href="https://fonts.googleapis.com/css2?family=Sniglet:wght@800&family=Roboto:wght@400;500;700&display=swap">
<style>
  :root {
    --ink: #000000;
    --white: #ffffff;
    --yellow: #f7c531;
    --green: #3fc41f;
    --blue: #5b8ef0;
    --band-blue: #2a4f9a;
    --band-deep: #1d3a78;
    --tile-violet: rgba(120, 80, 160, 0.18);
    --tile-red: rgba(170, 60, 60, 0.16);
    --tile-olive: rgba(140, 130, 40, 0.16);
    --tile-green: rgba(50, 140, 60, 0.16);
    --tile-teal: rgba(50, 110, 140, 0.18);
  }
  html, body {
    margin: 0;
    padding: 0;
    overflow: hidden;
    background: var(--ink);
  }
  .banner {
    position: relative;
    width: 1200px;
    height: 328px;
    overflow: hidden;
    background:
      linear-gradient(to bottom, rgba(0,0,0,0.85) 0%, rgba(0,0,0,0.35) 55%, rgba(0,0,0,0.55) 100%),
      linear-gradient(to right, var(--tile-violet), var(--tile-red) 25%, var(--tile-olive) 50%, var(--tile-green) 72%, var(--tile-teal) 100%),
      var(--ink);
    font-family: "Roboto", Arial, sans-serif;
    color: var(--white);
  }
  .brand-band {
    position: absolute;
    left: 0;
    top: 12px;
    width: 720px;
    height: 54px;
    background: linear-gradient(to right, var(--band-blue) 0%, var(--band-blue) 55%, rgba(42,79,154,0) 100%);
  }
  .byline-band {
    position: absolute;
    left: 0;
    top: 66px;
    width: 420px;
    height: 33px;
    background: linear-gradient(to right, var(--band-deep) 0%, var(--band-deep) 60%, rgba(29,58,120,0) 100%);
  }
  .brand-mark {
    position: absolute;
    left: 14px;
    top: 15px;
    width: 46px;
    height: 46px;
    border-radius: 50%;
    background: var(--yellow);
  }
  .brand-name {
    position: absolute;
    left: 80px;
    top: 15px;
    margin: 0;
    font-weight: 700;
    font-size: 33px;
    line-height: 46px;
    color: var(--white);
    white-space: nowrap;
  }
  .byline {
    position: absolute;
    left: 94px;
    top: 66px;
    margin: 0;
    font-weight: 400;
    font-size: 24px;
    line-height: 33px;
    color: var(--yellow);
  }
  .contact {
    position: absolute;
    right: 10px;
    top: 12px;
    text-align: right;
    font-size: 15.5px;
    line-height: 23px;
  }
  .contact p { margin: 0; }
  .contact .invite { font-weight: 700; }
  .contact .follow { color: var(--green); }
  .contact .free { color: var(--blue); }
  .contact .divider { font-weight: 400; color: #9aa8c8; }
  .studio-scene {
    position: absolute;
    left: 877px;
    top: 62px;
    width: 323px;
    height: 172px;
    background:
      radial-gradient(ellipse at 30% 40%, rgba(60,120,160,0.55), rgba(20,40,60,0.2) 55%, rgba(0,0,0,0) 75%),
      radial-gradient(ellipse at 80% 45%, rgba(70,100,200,0.5), rgba(0,0,0,0) 60%),
      linear-gradient(to bottom, #1a2530, #0a0d12);
    border-radius: 4px;
  }
  .headline {
    position: absolute;
    left: 0;
    width: 1132px;
    top: 106px;
    margin: 0;
    text-align: center;
    font-family: "Sniglet", "Arial Rounded MT Bold", sans-serif;
    font-weight: 800;
    font-size: 37px;
    line-height: 50px;
    text-shadow: 2px 2px 3px rgba(0,0,0,0.8);
  }
  .headline .line { display: block; }
  .headline .yellow { color: var(--yellow); }
  .headline .green { color: var(--green); }
  .headline .blue { color: var(--blue); }
  .topics {
    position: absolute;
    left: 0;
    width: 1198px;
    top: 232px;
    margin: 0;
    text-align: center;
    font-size: 21.5px;
    font-weight: 400;
    color: var(--white);
  }
</style>
</head>
<body>
  <header class="banner">
    <div class="brand-band"></div>
    <div class="byline-band"></div>
    <span class="brand-mark" aria-hidden="true"></span>
    <h1 class="brand-name">Cozy Nook Attic Sound</h1>
    <p class="byline">by Dale Whitford</p>

    <div class="contact">
      <p class="invite"><span class="follow">Follow</span> my Studio Renovation <span class="divider">|</span> <span class="free">Free</span> How-To’s</p>
      <p class="email">cozynookatticsound@postlark.net</p>
    </div>

    <div class="studio-scene" role="img" aria-label="Home studio desk with a condenser microphone in front of two monitors showing recording software"></div>

    <h2 class="headline">
      <span class="line">A <span class="yellow">Regular Joe</span> Blowin’ his <span class="green">Dough</span></span>
      <span class="line">on <span class="blue">Gear and Guitars</span></span>
    </h2>

    <p class="topics">Music + Gear + Livestreaming + Recording + DAW + Instruments + Vidora</p>
  </header>
</body>
</html>
```